Most captivating card ever!

Life Coach - Professional Adventurer - Entrepreneur
I need the worlds most amazing business card for my personal brand. This business card will mostly be used to give to prospective clients for life coaching and business coaching.
Be creative, be adventurous. It needs to stand out. Make people say.. I need this guy!
My background is as an entrepreneur and professional adventurer undertaking extreme expeditions. I am now moving into life coaching.
No specific design ideas, so you have full creativity. Show me your best.
Industry/Entity Type
Life Coaching
Contact Information for Business Card
Dan Pellow
itsdanp.com.au
0468215903
Colors
Designer to choose colors to be used in the design.
Look and feel

```html
<!DOCTYPE html>
<html lang="en">
<head>
<meta charset="utf-8">
<title>Dan Pellow – Business Card</title>
<link rel="stylesheet" href="https://fonts.googleapis.com/css2?family=Bebas+Neue&family=Montserrat:wght@400;500&display=swap">
<style>
  :root {
    --page: #ecebe8;
    --card: #1f1f1f;
    --accent: #dd752c;
    --name-grey: #cfcfcf;
    --text-light: #e6e6e6;
  }
  * { margin: 0; padding: 0; box-sizing: border-box; }
  html, body { width: 1200px; height: 800px; overflow: hidden; }
  body {
    background: var(--page);
    position: relative;
    font-family: "Montserrat", sans-serif;
  }
  .card {
    position: absolute;
    top: 259px;
    width: 445px;
    height: 251px;
    background: var(--card);
    overflow: hidden;
  }
  .card--front { left: 129px; }
  .card--back { left: 627px; }

  .accent-band {
    position: absolute;
    left: 0; top: 97px;
    width: 240px; height: 57px;
    background: var(--accent);
  }
  .name {
    font-family: "Bebas Neue", sans-serif;
    font-weight: 400;
    font-size: 37px;
    line-height: 33px;
    letter-spacing: 2.5px;
    color: var(--name-grey);
  }
  .card--front .name {
    position: absolute;
    left: 269px; top: 93px;
  }
  .roles {
    list-style: none;
    font-size: 11.5px;
    line-height: 15px;
    color: var(--text-light);
  }
  .roles li { position: relative; padding-left: 13px; }
  .roles li::before {
    content: "";
    position: absolute;
    left: 0; top: 6px;
    width: 4px; height: 4px;
    background: var(--accent);
  }
  .card--front .roles {
    position: absolute;
    left: 262px; top: 161px;
  }

  .edge-bar {
    position: absolute;
    top: 90px;
    width: 5px; height: 71px;
    background: var(--accent);
  }
  .edge-bar--left { left: 0; }
  .edge-bar--right { right: 0; }
  .card--back .name {
    position: absolute;
    right: 227px; top: 93px;
    text-align: right;
  }
  .name .hl { color: var(--accent); }
  .card--back .roles {
    position: absolute;
    left: 231px; top: 102px;
  }
  .card--back .roles li::before { background: var(--text-light); }
  .contact {
    position: absolute;
    left: 0; right: 0; top: 213px;
    text-align: center;
    font-size: 11.5px;
    color: var(--text-light);
  }
  .contact .label { color: var(--accent); }
  .contact .divider { margin: 0 6px; }
</style>
</head>
<body>
  <section class="card card--front" aria-label="Business card front">
    <div class="accent-band"></div>
    <h1 class="name">Dan<br>Pellow</h1>
    <ul class="roles">
      <li>Life Coach</li>
      <li>Professional Adventurer</li>
      <li>Entrepreneur</li>
    </ul>
  </section>

  <section class="card card--back" aria-label="Business card back">
    <div class="edge-bar edge-bar--left"></div>
    <div class="edge-bar edge-bar--right"></div>
    <h2 class="name"><span class="hl">D</span>A<span class="hl">N</span><br><span class="hl">P</span>EL<span class="hl">L</span>O<span class="hl">W</span></h2>
    <ul class="roles">
      <li>Life Coach</li>
      <li>Professional Adventurer</li>
      <li>Entrepreneur</li>
    </ul>
    <p class="contact">
      <span class="label">phone :</span> 046 821 5903
      <span class="divider">|</span>
      <span class="label">website :</span> itsdanp.com.au
    </p>
  </section>
</body>
</html>
```